HVAC Door Hanger- 4.25 inches by 11 inches

Hello We are using the Brightvale door hanger as an inspiration for our new door hanger. The company name is Corvant Home Services. Logo files attached. The Slogan needs to be added on the front with the Logo "Southern California’s Trusted Name in Home Services". Instead of the X protection plan, the name will be Full Shield by Corvant or Corvant Climate Keeper- The slogan for this package will be "Peace of Mind, For Every Season

```html
<!DOCTYPE html>
<html lang="en">
<head>
<meta charset="utf-8">
<title>Corvant Home Services – Door Hangers</title>
<link href="https://fonts.googleapis.com/css2?family=Oswald:wght@500;600;700&family=Montserrat:wght@500;600;700;800&family=Kaushan+Script&display=swap" rel="stylesheet">
<style>
  :root{
    --stage:#262626;
    --brand-blue:#1476b0;
    --deep-blue:#0d5f92;
    --alert-red:#e8202a;
    --ink:#111111;
    --text-dark:#2a2a2a;
    --white:#ffffff;
  }
  *{margin:0;padding:0;box-sizing:border-box}
  html,body{width:1200px;height:1200px;overflow:hidden;background:var(--stage)}
  .stage{position:relative;width:1200px;height:1200px}
  .hanger{position:absolute;top:50px;width:463px;height:1099px;background:var(--white);overflow:hidden}
  .hanger--front{left:107px}
  .hanger--back{left:647px}
  .hanger-cut{position:absolute;left:0;top:0;width:463px;height:260px;z-index:10}
  .abs{position:absolute}

  /* front */
  .front-photo{left:0;top:0;width:463px;height:700px;background:linear-gradient(180deg,#106493 0%,#1d6e9e 55%,#2a79a6 100%)}
  .front-headline{left:0;width:463px;top:240px;text-align:center;font-family:"Oswald",sans-serif;font-weight:500;color:var(--white);font-size:46px;line-height:46px;letter-spacing:-1px;transform:scaleX(.88)}
  .front-script{left:0;width:463px;text-align:center;font-family:"Kaushan Script",cursive;color:var(--white);font-size:104px;line-height:100px;white-space:nowrap}
  .front-script.home{top:345px;left:-8px}
  .front-script.services{top:440px;left:-16px;font-size:110px}
  .front-lower{left:0;top:0;width:463px;height:1099px}
  .season-main{left:0;width:463px;top:682px;text-align:center;font-family:"Oswald",sans-serif;font-weight:700;color:var(--alert-red);font-size:68px;line-height:68px;letter-spacing:-2px;transform:scaleX(.82)}
  .season-sub{left:0;width:463px;top:746px;text-align:center;font-family:"Oswald",sans-serif;font-weight:500;color:var(--ink);font-size:58px;line-height:58px;letter-spacing:-2px;transform:scaleX(.82)}
  .brand-block{left:42px;top:895px;width:380px}
  .brand-name{display:flex;align-items:center;gap:9px;font-family:"Montserrat",sans-serif;font-weight:800;color:var(--brand-blue);font-size:24px;line-height:30px;white-space:nowrap}
  .brand-dot{width:20px;height:20px;border-radius:50%;background:var(--brand-blue);flex:none}
  .brand-trades{margin-top:14px;font-family:"Montserrat",sans-serif;font-weight:700;color:var(--alert-red);font-size:12.5px;letter-spacing:2.1px;white-space:nowrap}

  .footer{left:0;top:976px;width:463px;height:123px;background:var(--brand-blue);color:var(--white);text-align:center}
  .phone{display:flex;justify-content:center;align-items:center;gap:8px;margin-top:17px;font-family:"Montserrat",sans-serif;font-weight:700;font-size:48px;line-height:52px}
  .phone svg{width:30px;height:30px}
  .web{font-family:"Montserrat",sans-serif;font-weight:600;font-size:23px;line-height:30px}

  /* back */
  .tile--vent{left:0;top:0;width:228px;height:255px;background:linear-gradient(160deg,#f4f4f4,#cfd3d6)}
  .tile--panel{left:234px;top:0;width:229px;height:283px;background:linear-gradient(150deg,#d8d4cc,#8f8a83)}
  .tile--plumber{left:0;top:261px;width:228px;height:240px;background:linear-gradient(150deg,#d6dde4,#3f66a6)}
  .tile--ac{left:234px;top:289px;width:229px;height:212px;background:linear-gradient(210deg,#2f55c9,#e7eaee)}
  .back-peak{left:0;top:0;width:463px;height:1099px}
  .plan-title{left:0;width:463px;top:440px;text-align:center;font-family:"Montserrat",sans-serif;font-weight:800;color:var(--alert-red);font-size:25px;line-height:28px}
  .plan-brand{left:0;width:463px;top:476px;display:flex;flex-direction:column;align-items:center}
  .plan-brand .brand-name{font-size:17px;line-height:20px;gap:6px}
  .plan-brand .brand-dot{width:13px;height:13px}
  .plan-brand .brand-trades{margin-top:3px;font-size:6px;letter-spacing:1px}

  .perks{left:24px;top:520px;width:420px;display:grid;grid-template-columns:213px 207px;row-gap:8px}
  .perk{display:flex;align-items:center;gap:7px;height:48px;font-family:"Montserrat",sans-serif;font-weight:500;font-size:13px;line-height:17px;color:var(--text-dark);white-space:nowrap}
  .perk-icon{width:46px;height:46px;flex:none}

  .offer-head{left:0;width:463px;top:692px;text-align:center;font-family:"Oswald",sans-serif;font-weight:700;color:var(--alert-red);font-size:36px;line-height:38px;letter-spacing:-1px;transform:scaleX(.8)}
  .offer-sub{left:0;width:463px;top:733px;text-align:center;font-family:"Oswald",sans-serif;font-weight:600;color:var(--brand-blue);font-size:30px;line-height:32px;letter-spacing:-1px;transform:scaleX(.8)}
  .deal{left:26px;top:773px;width:405px;height:184px;background:var(--alert-red);border-radius:20px;overflow:hidden;color:var(--white)}
  .deal-reg{position:absolute;right:-40px;top:-60px;width:190px;height:190px;border-radius:50%;background:var(--brand-blue)}
  .deal-reg-text{position:absolute;right:18px;top:6px;text-align:center;font-family:"Montserrat",sans-serif;font-weight:800;font-size:29px;line-height:36px}
  .deal-reg-text sup{font-size:15px;vertical-align:top;line-height:20px}
  .deal-title{position:absolute;left:22px;top:4px;font-family:"Oswald",sans-serif;font-weight:500;font-size:36px;line-height:38px;letter-spacing:-1px;transform:scaleX(.8);transform-origin:left;white-space:nowrap}
  .deal-price{position:absolute;left:20px;top:34px;font-family:"Oswald",sans-serif;font-weight:700;font-size:66px;line-height:66px;letter-spacing:-2px;transform:scaleX(.8);transform-origin:left;white-space:nowrap}
  .deal-price sup{font-size:32px;vertical-align:top;line-height:40px}
  .deal-list{position:absolute;left:22px;top:104px;width:370px;display:grid;grid-template-columns:198px 172px;row-gap:4px;font-family:"Oswald",sans-serif;font-weight:500;font-size:14px;line-height:15.5px;list-style:none;white-space:nowrap}
  .deal-list li{position:relative;padding-left:10px}
  .deal-list li::before{content:"";position:absolute;left:0;top:5px;width:5px;height:5px;border-radius:50%;background:var(--white)}
  .deal-rebate{position:absolute;left:0;bottom:0;width:405px;height:23px;background:var(--brand-blue);text-align:center;font-family:"Montserrat",sans-serif;font-weight:700;font-size:12.5px;line-height:23px;white-space:nowrap}
</style>
</head>
<body>
<main class="stage">

  <!-- Front -->
  <section class="hanger hanger--front">
    <div class="abs front-photo" role="img" aria-label="Blue-toned photo of a bright living room with sofa and pendant lights"></div>
    <h1 class="abs front-headline">SOUTHERN CALIFORNIA’S<br>TRUSTED NAME IN</h1>
    <div class="abs front-script home">Home</div>
    <div class="abs front-script services">Services</div>

    <svg class="abs front-lower" viewBox="0 0 463 1099" aria-hidden="true">
      <defs>
        <linearGradient id="houseFade" x1="0" y1="0" x2="0" y2="1">
          <stop offset="0" stop-color="#ffffff"/>
          <stop offset=".45" stop-color="#e6e6e6"/>
          <stop offset=".75" stop-color="#cfcfcf"/>
          <stop offset="1" stop-color="#ffffff"/>
        </linearGradient>
      </defs>
      <path d="M0,686 L231,578 L463,686 L463,976 L0,976 Z" fill="url(#houseFade)"/>
    </svg>
    <div class="abs" style="left:0;top:700px;width:463px;height:200px" role="img" aria-label="Faded greyscale photo of a suburban house and a technician's tool belt"></div>

    <h2 class="abs season-main">PEACE OF MIND</h2>
    <p class="abs season-sub">FOR EVERY SEASON</p>

    <div class="abs brand-block">
      <div class="brand-name"><span class="brand-dot"></span>Corvant Home Services</div>
      <div class="brand-trades">HEATING COOLING PLUMBING ELECTRICAL</div>
    </div>

    <footer class="abs footer">
      <div class="phone">
        <svg viewBox="0 0 24 24" aria-hidden="true"><path d="M6.6 10.8a15 15 0 0 0 6.6 6.6l2.2-2.2c.3-.3.7-.4 1-.2 1.1.4 2.3.6 3.6.6.6 0 1 .4 1 1V20c0 .6-.4 1-1 1A17 17 0 0 1 3 4c0-.6.4-1 1-1h3.5c.6 0 1 .4 1 1 0 1.3.2 2.5.6 3.6.1.3 0 .7-.2 1z" fill="#9fd3f2"/></svg>
        555.014.7290
      </div>
      <div class="web">www.corvanthome.com</div>
    </footer>

    <svg class="hanger-cut" viewBox="0 0 463 260" aria-hidden="true">
      <path d="M0,96 C70,112 130,116 178,105 A59,59 0 1 1 178,153 C130,142 70,148 0,172 Z" fill="var(--stage)"/>
    </svg>
  </section>

  <!-- Back -->
  <section class="hanger hanger--back">
    <div class="abs tile--vent" role="img" aria-label="Photo of a white wall radiator with a potted plant"></div>
    <div class="abs tile--panel" role="img" aria-label="Photo of hands testing an electrical breaker panel"></div>
    <div class="abs tile--plumber" role="img" aria-label="Photo of a plumber repairing pipes under a sink"></div>
    <div class="abs tile--ac" role="img" aria-label="Photo of a technician servicing a wall air conditioner"></div>

    <svg class="abs back-peak" viewBox="0 0 463 1099" aria-hidden="true">
      <path d="M0,497 L231,385 L463,497 L463,1099 L0,1099 Z" fill="var(--white)"/>
    </svg>

    <h2 class="abs plan-title">FULL SHIELD BY</h2>
    <div class="abs plan-brand">
      <div class="brand-name"><span class="brand-dot"></span>Corvant Home Services</div>
      <div class="brand-trades">HEATING COOLING PLUMBING ELECTRICAL</div>
    </div>

    <div class="abs perks">
      <div class="perk">
        <svg class="perk-icon" viewBox="0 0 46 46" aria-hidden="true"><circle cx="23" cy="23" r="22" fill="none" stroke="var(--alert-red)" stroke-width="1.5"/><circle cx="23" cy="23" r="19" fill="var(--deep-blue)"/><g stroke="#fff" stroke-width="1.8" fill="none"><rect x="14" y="18" width="18" height="13" rx="2"/><path d="M18 18v13M23 18v13M28 18v13M16 14c1-1 1-2 0-3M21 14c1-1 1-2 0-3M26 14c1-1 1-2 0-3"/></g></svg>
        <span>Annual Performance<br>Heating Tune-Up</span>
      </div>
      <div class="perk">
        <svg class="perk-icon" viewBox="0 0 46 46" aria-hidden="true"><circle cx="23" cy="23" r="22" fill="none" stroke="var(--alert-red)" stroke-width="1.5"/><circle cx="23" cy="23" r="19" fill="var(--deep-blue)"/><g stroke="#fff" stroke-width="2" stroke-linecap="round"><path d="M23 11v24M12.6 17l20.8 12M12.6 29l20.8-12"/></g></svg>
        <span>Annual Performance<br>A/C Tune-Up</span>
      </div>
      <div class="perk">
        <svg class="perk-icon" viewBox="0 0 46 46" aria-hidden="true"><circle cx="23" cy="23" r="22" fill="none" stroke="var(--alert-red)" stroke-width="1.5"/><circle cx="23" cy="23" r="19" fill="var(--deep-blue)"/><g stroke="#fff" stroke-width="1.8" fill="none"><path d="M12 22l11-9 11 9M15 20v12h16V20"/><path d="M18 24h10M18 28h8"/></g></svg>
        <span>10% Discount on Indoor<br>Air Quality Products</span>
      </div>
      <div class="perk">
        <svg class="perk-icon" viewBox="0 0 46 46" aria-hidden="true"><circle cx="23" cy="23" r="22" fill="none" stroke="var(--alert-red)" stroke-width="1.5"/><circle cx="23" cy="23" r="19" fill="var(--deep-blue)"/><g stroke="#fff" stroke-width="1.8" fill="none"><rect x="16" y="11" width="14" height="23" rx="3"/><path d="M23 17c-2 3-2 5 0 5s2-2 0-5M19 29h8"/></g></svg>
        <span>Yearly Water Heater<br>Flushing Service</span>
      </div>
      <div class="perk">
        <svg class="perk-icon" viewBox="0 0 46 46" aria-hidden="true"><circle cx="23" cy="23" r="22" fill="none" stroke="var(--alert-red)" stroke-width="1.5"/><circle cx="23" cy="23" r="19" fill="var(--deep-blue)"/><g stroke="#fff" stroke-width="1.8" fill="none" stroke-linecap="round"><path d="M14 32l12-12M29 14a4 4 0 1 0 3 3M14 14l18 18M14 14l3 0 0 3"/></g></svg>
        <span>Priority Scheduling for<br>Installations</span>
      </div>
      <div class="perk">
        <svg class="perk-icon" viewBox="0 0 46 46" aria-hidden="true"><circle cx="23" cy="23" r="22" fill="none" stroke="var(--alert-red)" stroke-width="1.5"/><circle cx="23" cy="23" r="19" fill="var(--deep-blue)"/><g stroke="#fff" stroke-width="1.8" fill="none" stroke-linecap="round"><path d="M19 14a10 10 0 1 1 0 18"/><path d="M13 23h14M22 18l5 5-5 5M15 19h4M15 27h4"/></g></svg>
        <span>Transferable to<br>New Owners</span>
      </div>
    </div>

    <h3 class="abs offer-head">MONTHLY SERVICE REDUCED</h3>
    <p class="abs offer-sub">From $29.99/Month to $19.99/Month</p>

    <div class="abs deal">
      <div class="deal-reg"></div>
      <div class="deal-reg-text">Reg.<br><sup>$</sup>176!</div>
      <div class="deal-title">HALF OFF SPECIAL</div>
      <div class="deal-price">ONLY <sup>$</sup>88</div>
      <ul class="deal-list">
        <li>AC System<br>Safety Inspection Tune Up</li>
        <li>Whole Home Water<br>Safety Inspection</li>
        <li>Standard Water Heater Flush</li>
        <li>Accessible Drain Cleaning</li>
      </ul>
      <div class="deal-rebate">GET UP TO $10,000 IN STATE &amp; FEDERAL REBATES !!!</div>
    </div>

    <footer class="abs footer">
      <div class="phone">
        <svg viewBox="0 0 24 24" aria-hidden="true"><path d="M6.6 10.8a15 15 0 0 0 6.6 6.6l2.2-2.2c.3-.3.7-.4 1-.2 1.1.4 2.3.6 3.6.6.6 0 1 .4 1 1V20c0 .6-.4 1-1 1A17 17 0 0 1 3 4c0-.6.4-1 1-1h3.5c.6 0 1 .4 1 1 0 1.3.2 2.5.6 3.6.1.3 0 .7-.2 1z" fill="#9fd3f2"/></svg>
        555.014.7290
      </div>
      <div class="web">www.corvanthome.com</div>
    </footer>

    <svg class="hanger-cut" viewBox="0 0 463 260" aria-hidden="true">
      <path d="M0,96 C70,112 130,116 178,105 A59,59 0 1 1 178,153 C130,142 70,148 0,172 Z" fill="var(--stage)"/>
    </svg>
  </section>

</main>
</body>
</html>
```